Webdesign für  Kranken- und Seniorenpflege
Webdesign für Kranken- und Seniorenpflege
Zielgruppe
Ambulante Kranken- und Seniorenpflege
Tagespflege in Limbach-Oberfrohna, Mittweida und Chemnitz
Palliativpflege
Aufgabenstellung
- Erstellung in Adobe Photoshop
- Orientieren Sie sich am Socialmedia-Auftritt des Kunden

```html
<!DOCTYPE html>
<html lang="de">
<head>
<meta charset="utf-8">
<title>Lindenhof Pflege – Ambulante Kranken- und Seniorenpflege</title>
<link href="https://fonts.googleapis.com/css2?family=Fira+Sans+Condensed:ital,wght@0,400;0,500;0,600;0,700;1,500;1,600&display=swap" rel="stylesheet">
<style>
:root{
  --crimson:#a4003a;
  --crimson-dark:#7e0f33;
  --yellow:#f9b000;
  --yellow-light:#fcc53a;
  --grey:#f3f4f6;
  --text:#1d1d1b;
  --white:#fff;
}
*{margin:0;padding:0;box-sizing:border-box}
html,body{width:1200px;height:5029px;overflow:hidden}
body{position:relative;font-family:"Fira Sans Condensed",sans-serif;color:var(--text);background:var(--white)}
.abs{position:absolute}
section,header,footer,nav{position:absolute;left:0;width:1200px}

/* header */
.site-header{top:0;height:250px;background:var(--white)}
.header-wave{position:absolute;top:0;left:0}
.brand{position:absolute;left:122px;top:48px;display:flex;align-items:center;gap:10px}
.brand-dot{width:62px;height:62px;border-radius:50%;background:var(--yellow)}
.brand-name{font-weight:700;font-size:22px;color:var(--crimson)}
.tagline{position:absolute;left:121px;top:182px;font-style:italic;font-weight:600;font-size:27px;color:var(--yellow)}
.meta-links{position:absolute;right:110px;top:32px;font-size:11px;color:var(--white)}
.header-mail{position:absolute;right:110px;top:54px;font-size:16px;color:var(--white);display:flex;gap:8px;align-items:center}
.header-phone{position:absolute;right:110px;top:100px;display:flex;gap:14px;align-items:center;color:var(--crimson-dark)}
.phone-badge{width:56px;height:56px;border-radius:50%;background:var(--crimson);display:flex;align-items:center;justify-content:center}
.phone-label{font-size:15px;font-weight:500;color:var(--text)}
.phone-number{font-size:38px;font-weight:600;line-height:1;color:var(--crimson-dark)}

/* nav */
.main-nav{top:250px;height:78px;background:linear-gradient(#ffffff,#eeeeee);display:flex;align-items:center;justify-content:center;font-size:14.5px}
.main-nav ul{list-style:none;display:flex;gap:0}
.main-nav li{padding:0 8px;border-left:1px solid #333;line-height:14px}
.main-nav li:first-child{border-left:none}
.social{position:absolute;right:115px;top:30px;display:flex;gap:10px}
.social span{width:20px;height:20px;border-radius:50%;background:var(--crimson)}

/* hero */
.hero{top:328px;height:720px;overflow:hidden}
.hero-photo{position:absolute;inset:0;background:linear-gradient(110deg,#e9e4dc 0%,#c8b8a8 35%,#8a2f3a 55%,#e2d8cb 75%,#d9b36a 100%)}
.hero-wave{position:absolute;left:0;bottom:0}
.hero-claim{position:absolute;left:121px;top:530px;font-style:italic;font-weight:600;font-size:42px;line-height:48px;color:var(--white)}
.slider-btn{position:absolute;width:46px;height:46px;border-radius:50%;background:rgba(255,255,255,.75);display:flex;align-items:center;justify-content:center}

/* locations */
.locations{top:1048px;height:392px;text-align:center}
.section-kicker{font-weight:600;font-size:22px;color:var(--crimson)}
.loc{position:absolute;display:flex;align-items:flex-end;gap:8px;font-size:29px;font-weight:500;color:var(--yellow)}
.loc small{display:block;font-size:18px;color:var(--crimson);text-align:center;line-height:20px}
.hq{position:absolute;left:514px;top:262px;width:160px;text-align:center;font-size:15px;font-weight:500}
.hq .rule{height:2px;background:var(--yellow);margin:8px 0 10px}

/* content blocks */
.block-title{font-weight:600;font-size:36px;line-height:40px}
.block-text{font-size:16.5px;line-height:22px}
.arrow-list{list-style:none}
.arrow-list li{display:flex;align-items:center;gap:14px;font-weight:600;font-size:14px}
.arrow-dot{flex:none;width:30px;height:30px;border-radius:50%;background:var(--yellow);display:flex;align-items:center;justify-content:center}
.btn{display:inline-block;padding:3px 20px;border-radius:12px;font-size:12px;font-weight:600}
.btn-crimson{background:var(--crimson);color:var(--white)}
.btn-white{background:var(--white);color:var(--crimson)}

.advice{top:1440px;height:497px;background:var(--grey)}
.advice-photo{position:absolute;left:197px;top:2px;width:310px;height:402px;background:linear-gradient(135deg,#c9c5bf,#8c8781 60%,#e4e2de)}
.care{top:1937px;height:541px;background:var(--crimson);color:var(--white)}
.care-photo{position:absolute;left:689px;top:0;width:511px;height:541px;border-top-left-radius:230px 120px;background:linear-gradient(135deg,#c8d4dc,#4f8bb2 45%,#a84558 80%,#7c2636)}
.daycare{top:2478px;height:566px;background:var(--grey)}
.carousel{position:absolute;left:273px;top:242px;width:697px;height:230px;display:flex}
.carousel > div{flex:1}
.quote-tile{background:linear-gradient(135deg,#e0a400,#c98f00);color:var(--white);padding:30px 22px;font-weight:600;font-size:16px;line-height:17px;position:relative}
.palliative{top:3044px;height:468px;background:var(--crimson);color:var(--white)}
.palliative-photo{position:absolute;left:0;top:0;width:501px;height:468px;border-top-left-radius:520px 110px;background:radial-gradient(circle at 60% 55%,#e9c1b4 0%,#b16e76 25%,#5a1530 70%,#3b0f22 100%)}
.palliative .small{font-size:10.5px;line-height:16px}

.heroes-title{top:3570px;text-align:center;font-weight:600;font-size:22px;color:var(--crimson)}
.heroes{top:3658px;height:537px;overflow:hidden}
.heroes-photo{position:absolute;inset:0;background:linear-gradient(90deg,#e4a213,#f5b21f 40%,#d89811 70%,#f6b522);opacity:.95}
.heroes-copy{position:absolute;left:0;width:1200px;text-align:center;color:var(--white)}

.news{top:4195px;height:500px}
.news-item{position:absolute;width:280px}
.news-item h3{font-weight:500;font-size:21px;line-height:24px;color:var(--yellow)}
.news-item p{font-size:10px;line-height:16px;margin:16px 0 12px}
.btn-tiny{font-size:9px;padding:2px 18px;border-radius:8px}

/* footer */
.site-footer{top:4663px;height:366px}
.footer-wave{position:absolute;top:0;left:0}
.footer-band{position:absolute;top:127px;left:0;width:1200px;height:239px;background:var(--crimson);color:var(--white)}
.foot-col{position:absolute;top:40px;font-size:10px;line-height:19.5px}
.foot-col.muted span{color:#d87e9b}
</style>
</head>
<body>

<header class="site-header">
  <svg class="header-wave" width="1200" height="250" viewBox="0 0 1200 250" aria-hidden="true">
    <path d="M295 0 C 470 120, 760 195, 1200 205 L1200 0 Z" fill="#f9b000"/>
  </svg>
  <div class="brand"><span class="brand-dot"></span><span class="brand-name">Lindenhof Pflege</span></div>
  <div class="tagline">Ambulante Kranken- und Seniorenpflege</div>
  <div class="meta-links">Impressum &nbsp;|&nbsp; Datenschutz</div>
  <div class="header-mail">
    <svg width="16" height="12" viewBox="0 0 16 12"><rect x=".5" y=".5" width="15" height="11" fill="none" stroke="#fff"/><path d="M.5 .5 8 7 15.5 .5" fill="none" stroke="#fff"/></svg>
    info@lindenhof-pflege.example
  </div>
  <div class="header-phone">
    <div class="phone-badge"><svg width="26" height="26" viewBox="0 0 24 24"><path d="M6.6 10.8a15 15 0 0 0 6.6 6.6l2.2-2.2c.3-.3.7-.4 1-.2 1.1.4 2.3.6 3.6.6.6 0 1 .4 1 1V20c0 .6-.4 1-1 1A17 17 0 0 1 3 4c0-.6.4-1 1-1h3.5c.6 0 1 .4 1 1 0 1.3.2 2.5.6 3.6.1.3 0 .7-.2 1z" fill="#fff"/></svg></div>
    <div><div class="phone-label">Wir sind jederzeit kostenfrei für Sie da.</div><div class="phone-number">0800 5552031</div></div>
  </div>
</header>

<nav class="main-nav">
  <ul>
    <li>Kranken- und Seniorenpflege</li><li>Tagespflege</li><li>Palliativpflege</li><li>Pflegeberatung</li><li>Standorte</li><li>Stellenangebote</li><li>Aktuelles</li>
  </ul>
  <div class="social"><span></span><span></span></div>
</nav>

<section class="hero">
  <div class="hero-photo" role="img" aria-label="Foto: Pflegerin und Seniorin mit Strickmützen lachen gemeinsam"></div>
  <svg class="hero-wave" width="1200" height="260" viewBox="0 0 1200 260" aria-hidden="true">
    <path d="M0 90 C 220 -10, 560 10, 1200 260 L0 260 Z" fill="#f9b000"/>
  </svg>
  <div class="slider-btn" style="left:30px;top:294px"><svg width="14" height="22"><path d="M12 2 3 11l9 9" fill="none" stroke="#a4003a" stroke-width="2"/></svg></div>
  <div class="slider-btn" style="right:30px;top:294px"><svg width="14" height="22"><path d="M2 2l9 9-9 9" fill="none" stroke="#a4003a" stroke-width="2"/></svg></div>
  <div class="hero-claim">Weil uns Menschen am Herzen liegen,<br>jeden Tag – Lindenhof Pflege!</div>
</section>

<section class="locations">
  <div class="section-kicker" style="position:absolute;left:0;width:1200px;top:42px">Unsere Standorte</div>
  <svg width="0" height="0"><defs><symbol id="pin" viewBox="0 0 20 26"><path d="M10 0a10 10 0 0 0-10 10c0 7 10 16 10 16s10-9 10-16A10 10 0 0 0 10 0z" fill="#a4003a"/><circle cx="10" cy="10" r="4" fill="#fff"/></symbol></defs></svg>
  <div class="loc" style="left:270px;top:100px"><svg width="22" height="28"><use href="#pin"/></svg>Chemnitz</div>
  <div class="loc" style="left:478px;top:100px"><svg width="22" height="28"><use href="#pin"/></svg>Limbach-Oberfrohna</div>
  <div class="loc" style="left:807px;top:100px"><svg width="22" height="28"><use href="#pin"/></svg>Mittweida</div>
  <div class="loc" style="left:270px;top:168px"><svg width="22" height="28"><use href="#pin"/></svg><span><small>Tagespflege</small>Chemnitz</span></div>
  <div class="loc" style="left:478px;top:168px"><svg width="22" height="28"><use href="#pin"/></svg><span><small>Tagespflege</small>Limbach-Oberfrohna</span></div>
  <div class="loc" style="left:807px;top:168px"><svg width="22" height="28"><use href="#pin"/></svg><span><small>Tagespflege</small>Mittweida</span></div>
  <div class="hq"><svg width="20" height="18" viewBox="0 0 20 18"><path d="M10 0 0 8h3v10h14V8h3z" fill="#f9b000"/></svg><div class="rule"></div>Firmensitz und Verwaltung</div>
</section>

<section class="advice">
  <div class="advice-photo" role="img" aria-label="Foto: älterer Herr schreibt an einem Tisch"></div>
  <div class="abs" style="left:585px;top:54px">
    <h2 class="block-title" style="color:var(--crimson)">Pflegeberatung</h2>
    <p class="block-text" style="margin-top:18px">In diesem Bereich erhalten Sie aktuelle Informationen –<br>die Ihnen helfen die Pflege und Betreuung Ihrer Angehörigen<br>weiter zu verbessern.</p>
    <ul class="arrow-list" style="margin-top:20px;color:var(--crimson)">
      <li style="height:47px"><span class="arrow-dot"><svg width="10" height="12"><path d="M2 1l6 5-6 5" fill="none" stroke="#a4003a" stroke-width="2"/></svg></span>Beratung, Hilfe bei Anträgen</li>
      <li style="height:47px"><span class="arrow-dot"><svg width="10" height="12"><path d="M2 1l6 5-6 5" fill="none" stroke="#a4003a" stroke-width="2"/></svg></span>Pflege-Info</li>
      <li style="height:47px"><span class="arrow-dot"><svg width="10" height="12"><path d="M2 1l6 5-6 5" fill="none" stroke="#a4003a" stroke-width="2"/></svg></span>Pflegekurse</li>
    </ul>
    <span class="btn btn-crimson" style="margin-top:14px">Mehr erfahren</span>
  </div>
</section>

<section class="care">
  <div class="care-photo" role="img" aria-label="Foto: junge Pflegerin umarmt eine Seniorin"></div>
  <div class="abs" style="left:197px;top:72px;width:420px">
    <h2 class="block-title">Kranken- &amp;<br>Seniorenpflege</h2>
    <p class="block-text" style="margin-top:18px;font-size:16px">Als inhabergeführtes Unternehmen liegen uns die persönliche, individuelle Betreuung und Versorgung von Pflegebedürftigen besonders am Herzen.</p>
    <ul class="arrow-list" style="margin-top:20px">
      <li style="height:45px"><span class="arrow-dot"><svg width="10" height="12"><path d="M2 1l6 5-6 5" fill="none" stroke="#a4003a" stroke-width="2"/></svg></span>So gewährleisten wir.</li>
      <li style="height:45px"><span class="arrow-dot"><svg width="10" height="12"><path d="M2 1l6 5-6 5" fill="none" stroke="#a4003a" stroke-width="2"/></svg></span>Wir lieben es, zu pflegen. Das erhalten von Sie uns.</li>
      <li style="height:52px"><span class="arrow-dot"><svg width="10" height="12"><path d="M2 1l6 5-6 5" fill="none" stroke="#a4003a" stroke-width="2"/></svg></span>Neben der eigentlichen Pflege ist uns die Entlastung<br>von Angehörigen besonders wichtig.</li>
      <li style="height:45px"><span class="arrow-dot"><svg width="10" height="12"><path d="M2 1l6 5-6 5" fill="none" stroke="#a4003a" stroke-width="2"/></svg></span>Wir bieten Ihnen…</li>
    </ul>
    <span class="btn btn-white" style="margin-top:38px;margin-left:57px">Mehr erfahren</span>
  </div>
</section>

<section class="daycare">
  <div class="abs" style="left:197px;top:76px">
    <h2 class="block-title" style="color:var(--crimson)">Tagespflege</h2>
    <p class="block-text" style="margin-top:22px;font-size:16.5px">In der Tagespflege bieten wir, neben der Integration in unsere Sozialgemeinschaft,<br>eine Rundum-Betreuung für Senioren mit interessanten und abwechslungsreichen Tagesaktivitäten.</p>
  </div>
  <div class="slider-btn" style="left:213px;top:334px;width:34px;height:34px;background:#fff"><svg width="10" height="16"><path d="M9 1 2 8l7 7" fill="none" stroke="#a4003a" stroke-width="1.5"/></svg></div>
  <div class="slider-btn" style="left:997px;top:334px;width:34px;height:34px;background:#fff"><svg width="10" height="16"><path d="M1 1l7 7-7 7" fill="none" stroke="#a4003a" stroke-width="1.5"/></svg></div>
  <div class="carousel">
    <div class="quote-tile">» Hier hat mein Vater<br>&nbsp;&nbsp;&nbsp;einen geregelten<br>&nbsp;&nbsp;&nbsp;Tagesablauf und<br>&nbsp;&nbsp;&nbsp;soziale Kontakte «<span style="position:absolute;left:140px;top:108px;font-size:11px;font-weight:500">Jens Albrecht</span></div>
    <div role="img" aria-label="Foto: Senioren beim gemeinsamen Basteln am Tisch" style="background:linear-gradient(135deg,#d8d0d6,#8a6e8c 55%,#c7b2a6)"></div>
    <div role="img" aria-label="Foto: Senioren sitzen im Garten unter Bäumen" style="background:linear-gradient(180deg,#6d8e3e,#a4b66a 55%,#5b6e3a)"></div>
  </div>
  <span class="btn btn-crimson abs" style="left:586px;top:498px">Mehr erfahren</span>
</section>

<section class="palliative">
  <div class="palliative-photo" role="img" aria-label="Foto: Sonnenstrahlen brechen durch einen Baumwipfel"></div>
  <div class="abs" style="left:585px;top:58px;width:420px">
    <h2 class="block-title" style="font-size:34px">Palliativ Pflege</h2>
    <div style="color:var(--yellow);font-weight:600;font-size:14px;margin-top:2px">Die letzten Tage und Stunden</div>
    <p class="small" style="margin-top:24px">Die Zeit des Sterbens eines nahestehenden Menschen ist für viele Angehörige und Freunde eine Zeit der Krise, Angst und der Unsicherheit.</p>
    <p class="small" style="margin-top:10px">Vielleicht geht es Ihnen auch so, dass Sie Fragen beschäftigen wie zum Beispiel:</p>
    <ul class="small" style="list-style:none;margin-top:6px;font-style:italic;font-weight:600;line-height:28px">
      <li><span style="color:var(--yellow)">●</span>&nbsp; Was geschieht denn im Sterben?</li>
      <li><span style="color:var(--yellow)">●</span>&nbsp; Wie kann ich helfen?</li>
      <li><span style="color:var(--yellow)">●</span>&nbsp; Ist es normal das der Sterbende Mensch nichts mehr essen und trinken möchte?</li>
    </ul>
    <p class="small" style="margin-top:6px">Auf diese und viele andere Fragen wissen wir auch nicht immer die absolut richtige Antwort, aber wir können Ihnen sehr viel erklären und helfen. Sei es bei einem persönlichen Gespräch oder bei der Hilfe der Versorgung Ihres geliebten Angehörigen.</p>
    <span class="btn btn-white" style="margin-top:22px">Mehr erfahren</span>
  </div>
</section>

<div class="abs heroes-title" style="left:0;width:1200px">Zeit für Helden</div>

<section class="heroes">
  <div class="heroes-photo" role="img" aria-label="Foto: Pflegeteams in Dienstkleidung, gelb eingefärbt"></div>
  <div class="heroes-copy" style="top:228px;font-size:34px;font-weight:600;line-height:41px">Bereichern Sie unser Unternehmen<br>mit ihrer Fachkompetenz und zögern Sie nicht lange!</div>
  <div class="heroes-copy" style="top:338px;font-size:20px;font-weight:500">Unsere Teams sind aufgeschlossen und mit Freude bei der Arbeit!</div>
  <div class="heroes-copy" style="top:390px"><span class="btn btn-white">Jetzt Bewerben</span></div>
</section>

<section class="news">
  <div class="section-kicker" style="position:absolute;left:0;width:1200px;top:64px;text-align:center">Aktuelle Einblicke</div>
  <article class="news-item" style="left:197px;top:138px">
    <h3>Sommerfest in der<br>Tagespflege „Lindengarten“</h3>
    <p>Sommerausklang in der Tagespflege „Lindengarten“ in Chemnitz. Bei warmen Temperaturen und viel Sonnenschein genossen die Tagesgäste ein buntes Programm auf unserer Terrasse. Unsere Betreuungskraft Carola sorgte für …</p>
    <span class="btn btn-crimson btn-tiny">Weiterlesen</span>
  </article>
  <article class="news-item" style="left:492px;top:138px">
    <h3>Wochenausklang am<br>Schwanenteich in Mittweida</h3>
    <p>Die vergangene Woche haben wir mit unseren Gästen aus der Tagespflege „Am Markt“ am Schwanenteich in Mittweida ausklingen lassen. Nach einem Spaziergang durch den Park gab es Kaffee mit Kuchen …</p>
    <span class="btn btn-crimson btn-tiny">Weiterlesen</span>
  </article>
  <article class="news-item" style="left:808px;top:138px">
    <h3>Maifest in der Tagespflege<br>„Am Markt“</h3>
    <p>Zu unserem Maifest in der Tagespflege „Am Markt“ in Mittweida erlebten unsere Gäste bei schönstem Wetter einen fröhlichen Tag. Mit leckerer Maibowle, Salaten und Bratwurst vom Grill war gesorgt …</p>
    <span class="btn btn-tiny" style="background:var(--yellow);color:#fff">Weiterlesen</span>
  </article>
  <div class="hq" style="top:364px;left:514px"><svg width="18" height="18" viewBox="0 0 18 18"><rect width="18" height="18" fill="#f9b000"/><rect x="4" y="5" width="10" height="2" fill="#fff"/><rect x="4" y="10" width="10" height="2" fill="#fff"/></svg><div class="rule"></div>Alle Beiträge lesen</div>
</section>

<footer class="site-footer">
  <svg class="footer-wave" width="1200" height="130" viewBox="0 0 1200 130" aria-hidden="true">
    <path d="M0 110 C 260 -40, 700 -30, 1200 128 L1200 130 L0 130 Z" fill="#f9b000"/>
  </svg>
  <div class="abs" style="left:240px;top:66px;display:flex;align-items:center;gap:8px">
    <span style="width:40px;height:40px;border-radius:50%;background:#fff"></span>
    <span style="font-weight:700;font-size:15px;color:var(--crimson)">Lindenhof Pflege</span>
  </div>
  <div class="abs" style="left:372px;top:34px;font-style:italic;font-weight:600;font-size:28px;line-height:37px;color:#fff">Lindenhof Pflege in<br>Chemnitz, Limbach-Oberfrohna und Mittweida</div>

  <div class="footer-band">
    <div class="foot-col" style="left:121px">Lindenhof Pflege<br>Kranken- &amp; Seniorenpflege<br>Tagespflege<br>Palliativ Pflege<br>Pflege-Info<br>Pflegeberatung<br>Pflegekurse</div>
    <div class="foot-col" style="left:254px"><b>Standorte:</b><br>Chemnitz<br>Limbach-Oberfrohna<br>Mittweida<br>Tagespflege Chemnitz<br>Tagespflege Limbach-Oberfrohna<br>Tagespflege Mittweida</div>
    <div class="foot-col muted" style="left:412px">Stellenangebote<br>Verwaltung<br>Aktuelle Meldungen<br><br><br><span>Impressum</span><br><span>Datenschutz</span></div>
    <div class="abs" style="left:121px;top:193px;font-size:8px">Copyright © Lindenhof Pflege 2022</div>
    <div class="abs" style="right:115px;top:34px;display:flex;gap:14px;align-items:center">
      <div class="phone-badge" style="background:var(--yellow)"><svg width="26" height="26" viewBox="0 0 24 24"><path d="M6.6 10.8a15 15 0 0 0 6.6 6.6l2.2-2.2c.3-.3.7-.4 1-.2 1.1.4 2.3.6 3.6.6.6 0 1 .4 1 1V20c0 .6-.4 1-1 1A17 17 0 0 1 3 4c0-.6.4-1 1-1h3.5c.6 0 1 .4 1 1 0 1.3.2 2.5.6 3.6.1.3 0 .7-.2 1z" fill="#fff"/></svg></div>
      <div><div style="font-size:14px;color:var(--yellow);font-weight:500">Wir sind jederzeit kostenfrei für Sie da.</div><div style="font-size:38px;font-weight:600;line-height:1">0800 5552031</div></div>
    </div>
    <div class="abs" style="right:115px;top:129px;font-size:16px;display:flex;gap:8px;align-items:center">
      <svg width="16" height="12" viewBox="0 0 16 12"><rect x=".5" y=".5" width="15" height="11" fill="none" stroke="#fff"/><path d="M.5 .5 8 7 15.5 .5" fill="none" stroke="#fff"/></svg>
      info@lindenhof-pflege.example
    </div>
    <div class="abs" style="right:115px;top:160px;display:flex;gap:10px">
      <span style="width:20px;height:20px;border-radius:50%;background:#fff"></span>
      <span style="width:20px;height:20px;border-radius:50%;background:#fff"></span>
    </div>
  </div>
</footer>

</body>
</html>
```